Trade show flier

Need a two sided flier for a trade show that will go with the trade show banner you are designing for us. We have included some information we would like to see o the flier. We do need to work on the content. If you can start a design, we can work on the content. This must be done by 3/12/2018

Manufacturing companies

Trade

```html
<!DOCTYPE html>
<html lang="en">
<head>
<meta charset="utf-8">
<title>Linkway Systems – Trade Show Flier</title>
<link href="https://fonts.googleapis.com/css2?family=Questrial&display=swap" rel="stylesheet">
<style>
  :root {
    --backdrop: #e6e7e9;
    --paper: #ffffff;
    --panel-grey: #f2f2f2;
    --brand-blue: #2a64a8;
    --brand-blue-soft: #4f7fbf;
    --navy: #24406e;
    --charcoal: #333437;
    --ink: #3a3a3c;
    --muted-ink: #55575a;
    --badge: #d9dbde;
  }
  * { box-sizing: border-box; margin: 0; padding: 0; }
  html, body { width: 1200px; height: 830px; overflow: hidden; }
  body {
    background: var(--backdrop);
    font-family: "Questrial", "Century Gothic", sans-serif;
    color: var(--ink);
    position: relative;
  }
  .page {
    position: absolute;
    top: 71px;
    width: 489px;
    height: 688px;
    background: var(--paper);
    box-shadow: 0 6px 18px rgba(0,0,0,0.18);
    overflow: hidden;
  }
  .page--front { left: 81px; }
  .page--back { left: 630px; }

  /* Front */
  .front-header {
    position: absolute; left: 7px; top: 7px; width: 476px; height: 130px;
    background: var(--panel-grey);
  }
  .brand {
    position: absolute; left: 37px; top: 28px;
    display: flex; align-items: center; gap: 8px;
    color: var(--brand-blue); font-size: 26px; letter-spacing: 0.5px;
  }
  .brand__dot {
    width: 28px; height: 28px; border-radius: 50%; background: var(--brand-blue);
  }
  .hero { position: absolute; left: 7px; top: 49px; width: 476px; height: 373px; }

  .profile {
    position: absolute; left: 42px; top: 408px; width: 392px; height: 134px;
    background: var(--charcoal);
  }
  .profile__label {
    position: absolute; left: 70px; top: 389px; width: 228px; height: 38px;
    background: #3f6594; color: #fff;
    font-size: 15px; letter-spacing: 3.2px;
    display: flex; align-items: center; justify-content: center;
  }
  .profile__text {
    position: absolute; left: 38px; top: 38px; width: 318px;
    color: #f1f1f1; font-size: 7.6px; line-height: 14.6px;
    letter-spacing: 0.55px; text-align: justify;
  }
  .statement { position: absolute; top: 564px; width: 165px; }
  .statement--vision { left: 80px; }
  .statement--mission { left: 272px; }
  .statement h2 {
    font-weight: 400; font-size: 15px; letter-spacing: 3.4px; color: var(--charcoal);
  }
  .statement p {
    margin-top: 8px; font-size: 7.6px; line-height: 14.6px; letter-spacing: 0.7px;
  }
  .divider {
    position: absolute; left: 238px; top: 570px; width: 1px; height: 86px;
    background: #c9c9c9;
  }

  /* Back */
  .services-panel {
    position: absolute; left: 31px; top: 6px; width: 196px; height: 510px;
    background: var(--panel-grey);
  }
  .section-icon {
    position: absolute; border-radius: 50%;
    display: flex; align-items: center; justify-content: center;
  }
  .section-icon--services { left: 46px; top: 34px; width: 35px; height: 35px; background: var(--brand-blue); }
  .section-icon--support { left: 262px; top: 34px; width: 35px; height: 35px; background: #8aa9d3; }
  .section-title {
    position: absolute; color: var(--brand-blue); font-size: 12.6px;
    letter-spacing: 1px; line-height: 15px;
  }
  .section-title--services { left: 94px; top: 47px; }
  .section-title--support { left: 430px; }
  .section-title--support { left: 430px; top: 41px; }
  .bullet-list { position: absolute; list-style: none; font-size: 7.2px; line-height: 11.4px; color: var(--ink); }
  .bullet-list li { position: relative; padding-left: 7px; }
  .bullet-list li::before {
    content: ""; position: absolute; left: 0; top: 4px;
    width: 3px; height: 3px; border-radius: 50%; background: var(--brand-blue);
  }
  .bullet-list--services { left: 45px; top: 88px; width: 172px; }
  .bullet-list--services li { margin-bottom: 11.4px; }
  .bullet-list--support { left: 265px; top: 88px; width: 190px; }
  .bullet-list--support li { margin-bottom: 11.2px; }

  .promise-band {
    position: absolute; left: 6px; top: 516px; width: 475px; height: 65px;
    background: linear-gradient(100deg, #2c4d7e 0%, #3a629a 45%, #284675 100%);
    color: #fff; font-size: 8.4px; line-height: 16px; padding: 14px 0 0 45px;
  }
  .partners-label {
    position: absolute; left: 26px; top: 571px; width: 229px; height: 29px;
    background: var(--charcoal); color: #fff; font-size: 11px; letter-spacing: 0.6px;
    display: flex; align-items: center; padding-left: 25px;
  }
  .partner-badge {
    position: absolute; width: 80px; height: 18px; border-radius: 3px; background: var(--badge);
  }
</style>
</head>
<body>

<section class="page page--front">
  <div class="front-header"></div>
  <svg class="hero" viewBox="0 0 476 373" role="img" aria-label="Black-and-white photograph of three businessmen reviewing a plan, beneath a faceted blue geometric band">
    <defs>
      <linearGradient id="photoTone" x1="0" y1="0" x2="1" y2="1">
        <stop offset="0" stop-color="#b9bcc0"/>
        <stop offset="0.5" stop-color="#6e7174"/>
        <stop offset="1" stop-color="#a5a8ab"/>
      </linearGradient>
      <linearGradient id="bandTone" x1="0" y1="0" x2="1" y2="0">
        <stop offset="0" stop-color="#2f5a93"/>
        <stop offset="0.5" stop-color="#4a77b3"/>
        <stop offset="1" stop-color="#244a80"/>
      </linearGradient>
    </defs>
    <rect x="0" y="130" width="476" height="243" fill="url(#photoTone)"/>
    <polygon points="0,124 476,50 476,170 300,210 0,190" fill="url(#bandTone)"/>
  </svg>
  <div class="brand"><span class="brand__dot"></span>Linkway Systems</div>

  <div class="profile">
    <p class="profile__text">Established in 2006, Linkway Systems is a Managed IT Service firm providing exceptional IT consultation and support for businesses in the California with 20 – 1000 employees. Our personable, reliable and professional team empowers our clients to make their IT infrastructure a strategic asset.</p>
  </div>
  <div class="profile__label">COMPANY PROFILE</div>

  <div class="statement statement--vision">
    <h2>OUR VISION</h2>
    <p>To provide a customer experience that provides value and enables technology collaboration effortlessly.</p>
  </div>
  <div class="divider"></div>
  <div class="statement statement--mission">
    <h2>OUR MISSION</h2>
    <p>Innovative collaboration to improve business process by leveraging technology that empowers organizations to implement a roadmap to success.</p>
  </div>
</section>

<section class="page page--back">
  <div class="services-panel"></div>
  <div class="section-icon section-icon--services">
    <svg width="18" height="20" viewBox="0 0 18 20" fill="none" stroke="#fff" stroke-width="1.3">
      <circle cx="9" cy="6" r="4"/><path d="M1 19c0-4 3.5-6.5 8-6.5s8 2.5 8 6.5"/>
    </svg>
  </div>
  <div class="section-title section-title--services">SERVICES</div>

  <ul class="bullet-list bullet-list--services">
    <li>Managed Services – Proactive support, remediation and maintenance of your technology infrastructure, 24/7.</li>
    <li>Backup and Business Continuity – Secure your data while minimizing downtime.</li>
    <li>Virtualization – Increase IT flexibility and scalability while minimizing hardware resources.</li>
    <li>Voice Collaboration – Voice-over-IP (VOIP) Design and Deployment.</li>
    <li>Cloud Services – Leverage cloud support services for remote access and or business continuity.</li>
    <li>Security Services – Multi-layered approach to addressing your network security.</li>
    <li>Wireless Services – Secure connectivity and centralized management for wireless endpoint devices.</li>
    <li>Procurement Services – Procurement of industry standard business class product.</li>
    <li>Project Collaboration – Strategic technology roadmaps that address company business goals.</li>
    <li>Surveillance Services - Intelligent network security video solutions.</li>
  </ul>

  <div class="section-icon section-icon--support">
    <svg width="14" height="17" viewBox="0 0 14 17" fill="none" stroke="#fff" stroke-width="1.2">
      <rect x="1" y="1" width="12" height="15" rx="1"/><path d="M4 6h6M4 9h6M4 12h6"/>
    </svg>
  </div>
  <div class="section-title section-title--support" style="left:306px">OUR COMMON GROUND<br>MANAGED SERVICES<br>SUPPORT INCLUDE</div>

  <ul class="bullet-list bullet-list--support">
    <li>Team of industry certified Network Engineers</li>
    <li>Remote support (Weekdays 7am – 6pm)</li>
    <li>Onsite support (Weekdays 7am – 6pm)</li>
    <li>24x7 network monitoring and remediation</li>
    <li>Daily proactive maintenance</li>
    <li>Managed antivirus software</li>
    <li>Managed ransomware protection</li>
    <li>Ticketing portal to track open tickets and resolutions</li>
    <li>Vendor management</li>
    <li>Network Documentation Management</li>
    <li>Software License Management</li>
    <li>Technology procurement</li>
    <li>Monitoring of existing backup systems and data recovery</li>
    <li>Business continuity planning</li>
    <li>Network and data security planning and testing</li>
    <li>Quarterly IT meetings</li>
  </ul>

  <div class="promise-band">We provide a great customer service experience with a simplified, cost-effective approach to<br>IT that leverages certified technical professionals with industry standard skills and knowledge.</div>
  <div class="partners-label">OUR TECHNOLOGY PARTNERS</div>

  <div class="partner-badge" style="left:54px;top:619px"></div>
  <div class="partner-badge" style="left:173px;top:619px"></div>
  <div class="partner-badge" style="left:273px;top:619px"></div>
  <div class="partner-badge" style="left:362px;top:619px"></div>
  <div class="partner-badge" style="left:54px;top:650px"></div>
  <div class="partner-badge" style="left:173px;top:650px"></div>
  <div class="partner-badge" style="left:273px;top:650px"></div>
  <div class="partner-badge" style="left:362px;top:650px"></div>
</section>

</body>
</html>
```